Photoshop Design Project

Just looking to use some existing element in emails and printed flyers for a lunch menu promo.

I am attaching a menu in progress to reference only the front page design of a chalkboard, chalk fonts, tagline of :Trade the Same Old Plate for Midday Fresh Bites. Its on the front of the menu.

I just want to drop in a photo of each on three separate pieces with description.

THe design should not be a match to the front of the menu, just utilize its elements. the design is not a lead at all, these should remain familiar with the front of the menu, but please use the elements to your design preference.

Ok to submit one layout that we can repeat, or ok to submit three different versions

Must stick with the colors though, they are brand color combo, not exact by color code, but the oranges and the browns need to stay somewhere and in some capacity.
SO menu attached, check out the front cover for inspirations, to go in email sends embedded, and to print as a flyer.

There are also three images attached they are the to be dropped into each piece, with a desciption
Updates

Reason: seems to be too many questions and I wasnt getting anywhere.. To clarify...One Design Piece (one page), three separate items, same peice, however three total. one for each product photo supplied

I moved the deadline back as there were many questions. To clarify, one design piece to be reused for three different products (sandwiches in this case) Same piece, but one for each sandwich.

I posted a file called Artsquare that now has each photo partnered with its title and description

Target Market(s)

hungry people looking for lunch

Industry/Entity Type

Promo

Requirements
Must have
• Attached Menu front page elements, of chalkboard, chalk font existing front colors.

```html
<!DOCTYPE html>
<html lang="en">
<head>
<meta charset="utf-8">
<title>Spicy Roast Beef Sandwich – Lunch Promo</title>
<link rel="stylesheet" href="https://fonts.googleapis.com/css2?family=Cabin+Sketch:wght@400;700&family=Gelasio:wght@400&display=swap">
<style>
  :root {
    --board-dark: #161616;
    --board-mid: #2a2a2a;
    --chalk-white: #f4f2ee;
    --brand-orange: #e2661f;
    --crust-brown: #c08a52;
    --beef-brown: #7a4f45;
    --plate-white: #e6e4e0;
    --cloth-tan: #d6c28c;
  }
  html, body {
    margin: 0;
    padding: 0;
    overflow: hidden;
    background: var(--board-dark);
  }
  .promo-card {
    position: relative;
    width: 837px;
    height: 1200px;
    overflow: hidden;
    background: radial-gradient(ellipse at 50% 30%, var(--board-mid) 0%, var(--board-dark) 80%);
  }
  .item-title {
    position: absolute;
    top: 112px;
    left: 0;
    width: 837px;
    margin: 0;
    text-align: center;
    font-family: "Cabin Sketch", cursive;
    font-weight: 400;
    font-size: 60px;
    line-height: 62px;
    letter-spacing: 1px;
    color: var(--chalk-white);
  }
  .item-description {
    position: absolute;
    top: 340px;
    left: 0;
    width: 837px;
    height: 200px;
  }
  .item-description text {
    font-family: "Gelasio", Georgia, serif;
    font-size: 44px;
    fill: var(--brand-orange);
  }
  .product-photo {
    position: absolute;
    left: 0;
    top: 565px;
    width: 837px;
    height: 635px;
    background: linear-gradient(180deg,
      var(--crust-brown) 0%,
      var(--beef-brown) 45%,
      var(--crust-brown) 62%,
      var(--plate-white) 80%,
      var(--cloth-tan) 100%);
  }
</style>
</head>
<body>
  <main class="promo-card">
    <h1 class="item-title">Spicy Roast Beef Sandwich<br>with Danish Smelly Cheese</h1>

    <svg class="item-description" viewBox="0 340 837 200" aria-label="Sprouts, fresh basil, onions and Chili Sauce on a fresh Ciabatta Roll">
      <defs>
        <path id="arc-line-one" d="M 134 420 Q 414 368 694 420"/>
        <path id="arc-line-two" d="M 37 508 Q 421 431 806 508"/>
      </defs>
      <text><textPath href="#arc-line-one" textLength="560" lengthAdjust="spacingAndGlyphs">Sprouts, fresh basil, onions</textPath></text>
      <text><textPath href="#arc-line-two" textLength="775" lengthAdjust="spacingAndGlyphs">and Chili Sauce on a fresh Ciabatta Roll</textPath></text>
    </svg>

    <div class="product-photo" role="img" aria-label="Photo of a roast beef sandwich on a ciabatta roll with melted cheese, basil and sprouts, served on a white plate"></div>
  </main>
</body>
</html>
```